Healthcare IT company looking for business card design

We develop IT systems for healthcare that significantly reduces cost and improves quality.

We want a business card design that is professional and clean, and using the colors in our logo.

Target Market(s)

Doctors and decision makers in the healthcare industry

Industry/Entity Type

Healthcare

Contact Information for Business Card

It should include
Name and title, address, telephone

Tobias Vrenholt, CEO
+46 712 418257
tobias@kelvaro.se

Font styles to use
Serif

Colors
0355a3
ed282f

Requirements
Must have
• Clean design
• Professional feel
Nice to have
• N/A
Should not have
• N/A

```html
<!DOCTYPE html>
<html lang="en">
<head>
<meta charset="utf-8">
<title>Kelvaro business cards</title>
<link rel="stylesheet" href="https://fonts.googleapis.com/css2?family=Open+Sans:wght@400;600;700&display=swap">
<style>
  :root {
    --brand-blue: #0355a3;
    --brand-red: #ed282f;
    --paper: #ffffff;
    --backdrop: #2b2b2b;
    --ink-light: #ffffff;
  }
  * { margin: 0; padding: 0; box-sizing: border-box; }
  html, body { width: 1200px; height: 907px; overflow: hidden; }
  body {
    background: var(--backdrop);
    font-family: "Open Sans", Arial, sans-serif;
    position: relative;
  }
  .card {
    position: absolute;
    width: 580px;
    height: 340px;
    overflow: hidden;
    box-shadow: 0 10px 30px rgba(0,0,0,.45);
  }
  /* Front */
  .card--front { left: 50px; top: 80px; background: var(--paper); }
  .front__panel {
    position: absolute;
    left: 300px; top: 0;
    width: 280px; height: 214px;
    background: var(--brand-blue);
    border-bottom: 5px solid var(--brand-red);
  }
  .wordmark {
    position: absolute;
    font-weight: 700;
    letter-spacing: -1px;
    line-height: 1;
    white-space: nowrap;
  }
  .card--front .wordmark {
    left: 40px; top: 120px;
    font-size: 60px;
    color: var(--brand-blue);
  }
  .contact {
    position: absolute;
    left: 24px; top: 30px;
    color: var(--ink-light);
    font-size: 12.5px;
    line-height: 1.5;
  }
  .contact__name { font-weight: 700; font-size: 14px; }
  .contact__title { margin-bottom: 8px; }
  .contact__address { margin-bottom: 8px; }
  .contact__row { display: flex; align-items: center; gap: 8px; margin-top: 3px; }
  .contact__icon {
    width: 16px; height: 16px;
    background: var(--brand-red);
    border-radius: 2px;
    display: flex; align-items: center; justify-content: center;
    flex: none;
  }
  /* Back */
  .card--back { left: 570px; top: 487px; background: var(--brand-red); }
  .back__map {
    position: absolute;
    left: 60px; top: 40px;
    width: 460px; height: 250px;
    border-radius: 40%;
    background: radial-gradient(ellipse at center, rgba(160,20,25,.35), rgba(237,40,47,0) 70%);
  }
  .card--back .wordmark {
    left: 0; right: 0; top: 118px;
    text-align: center;
    font-size: 76px;
    color: var(--ink-light);
  }
  .web {
    position: absolute;
    left: 110px; right: 40px; top: 236px;
    display: flex; align-items: center; gap: 12px;
    color: var(--ink-light);
    font-size: 17px;
    letter-spacing: 1px;
  }
  .web__rule { flex: 1; height: 1px; background: var(--ink-light); }
</style>
</head>
<body>
  <section class="card card--front">
    <div class="wordmark">Kelvaro</div>
    <div class="front__panel">
      <div class="contact">
        <p class="contact__name">Tobias Vrenholt</p>
        <p class="contact__title">Ceo</p>
        <p class="contact__address">Street Name, City Name,<br>zip code - 00000</p>
        <p class="contact__row">
          <span class="contact__icon"><svg width="10" height="10" viewBox="0 0 10 10"><path d="M2 1 L4 1 L4.6 3 L3.4 3.8 Q4.4 5.8 6.2 6.6 L7 5.4 L9 6 L9 8 Q8.6 9 7.6 9 Q1 8.4 1 2.4 Q1 1.4 2 1 Z" fill="#fff"/></svg></span>
          +46 712 418257
        </p>
        <p class="contact__row">
          <span class="contact__icon"><svg width="10" height="8" viewBox="0 0 10 8"><rect x="0.5" y="0.5" width="9" height="7" fill="none" stroke="#fff"/><path d="M0.5 0.5 L5 4.5 L9.5 0.5" fill="none" stroke="#fff"/></svg></span>
          tobias@kelvaro.se
        </p>
        <p class="contact__row">
          <span class="contact__icon"><svg width="10" height="10" viewBox="0 0 10 10"><circle cx="5" cy="5" r="4.3" fill="none" stroke="#fff"/><ellipse cx="5" cy="5" rx="2" ry="4.3" fill="none" stroke="#fff"/><path d="M0.7 5 H9.3" stroke="#fff"/></svg></span>
          www.kelvaro.se
        </p>
      </div>
    </div>
  </section>

  <section class="card card--back">
    <div class="back__map" role="img" aria-label="Faint dotted world map in the background"></div>
    <div class="wordmark">Kelvaro</div>
    <div class="web"><span class="web__rule"></span><span>www.kelvaro.se</span><span class="web__rule"></span></div>
  </section>
</body>
</html>
```